Business Card design for construction company

I would like a business card design for a construction company - Harlow Constructions. I have attached the ai logo file for use. I would like the card to be very smart and clean and incorporate only white and the two colours in the logo. I would like the card to have two sides. One side can just have the logo, the other with the relevant information.

Target Market(s)

Building and Construction Clients

Industry/Entity Type

Business

Contact Information for Business Card

Name: Tom Pardoe
Company: Harlow Constructions Pty Limited
Address: 14 Mallee Crescent Carrow Vale 2093
Phone: 0427 531 068
Email: tomp@harlowbuild-example.com.au

Font styles to use
Serif
Sans Serif

Requirements
Must have
• Details noted above
• Logo as provided
• Colours as in logo
• Square edges
• A font that compliments the logo
Should not have
• Any colour other than white and those in logo
• Rounded edges

```html
<!DOCTYPE html>
<html lang="en">
<head>
<meta charset="utf-8">
<title>Harlow Constructions – Business Card</title>
<link rel="stylesheet" href="https://fonts.googleapis.com/css2?family=Courier+Prime:wght@700&family=Montserrat:wght@300;400;600&display=swap">
<style>
  :root {
    --charcoal: #3c474f;
    --sky: #3ec3ef;
    --paper: #ffffff;
    --backdrop: #b3c3d0;
    --sky-soft: #d6eef8;
    --charcoal-soft: #dfe4e8;
  }
  * { box-sizing: border-box; margin: 0; padding: 0; }
  html, body { width: 1200px; height: 1120px; overflow: hidden; }
  body {
    background: var(--backdrop);
    display: flex;
    flex-direction: column;
    align-items: center;
    justify-content: center;
    gap: 64px;
    font-family: "Montserrat", sans-serif;
  }
  .card {
    position: relative;
    width: 760px;
    height: 464px;
    box-shadow: 0 8px 24px rgba(40, 55, 70, 0.18);
  }
  .card--front {
    background: var(--charcoal);
    display: flex;
    align-items: center;
    justify-content: center;
  }
  .brand-name {
    color: var(--paper);
    font-weight: 400;
    font-size: 64px;
    letter-spacing: 0.14em;
  }
  .card--back { background: var(--paper); }
  .rule {
    position: absolute;
    left: 0;
    top: 298px;
    width: 470px;
    height: 3px;
    background: var(--charcoal);
  }
  .skyline-area {
    position: absolute;
    left: 470px;
    top: 120px;
    width: 290px;
    height: 181px;
    background: linear-gradient(90deg, var(--charcoal-soft), var(--sky-soft));
  }
  .identity {
    position: absolute;
    left: 70px;
    top: 196px;
  }
  .identity__name {
    font-size: 50px;
    line-height: 1;
    letter-spacing: 0.02em;
    color: var(--charcoal);
    font-weight: 300;
  }
  .identity__first { color: var(--sky); font-weight: 600; }
  .identity__company {
    margin-top: 8px;
    font-family: "Courier Prime", monospace;
    font-weight: 700;
    font-size: 13px;
    letter-spacing: 0.14em;
    color: var(--charcoal);
  }
  .contact {
    position: absolute;
    right: 70px;
    top: 330px;
    text-align: right;
    color: var(--charcoal);
    font-style: normal;
    font-weight: 300;
    font-size: 19px;
    line-height: 1.55;
  }
</style>
</head>
<body>
  <section class="card card--front" aria-label="Card front">
    <span class="brand-name">HARLOW</span>
  </section>

  <section class="card card--back" aria-label="Card back">
    <div class="rule" aria-hidden="true"></div>
    <div class="skyline-area" role="img" aria-label="Line illustration of a city skyline in charcoal and sky blue"></div>

    <div class="identity">
      <h1 class="identity__name"><span class="identity__first">TOM</span> PARDOE</h1>
      <p class="identity__company">HARLOW CONSTRUCTIONS PTY LIMITED</p>
    </div>

    <address class="contact">
      14 Mallee Crescent Carrow Vale 2093<br>
      0427 531 068<br>
      tomp@harlowbuild-example.com.au
    </address>
  </section>
</body>
</html>
```